Restaurant Facility Equipment & Store Maintenance/

I need a flyer showing commercial/industrial kitchen equipment photos we work on Hot Equipment & Cold Equipment and offer many services. see attached highlights

```html
<!DOCTYPE html>
<html lang="en">
<head>
<meta charset="utf-8">
<title>Restaurant Facility Equipment &amp; Store Maintenance Flyer</title>
<link href="https://fonts.googleapis.com/css2?family=Bebas+Neue&family=Poppins:wght@400;500;600;700;800&display=swap" rel="stylesheet">
<style>
  :root {
    --red: #d11a2e;
    --ink: #232323;
    --white: #ffffff;
    --backdrop: #878787;
    --steel-light: #dfe3e6;
    --steel-mid: #a9b0b5;
    --steel-dark: #5d6468;
  }
  * { margin: 0; padding: 0; box-sizing: border-box; }
  html, body { width: 996px; height: 1200px; overflow: hidden; }
  body { background: var(--backdrop); font-family: "Poppins", sans-serif; }

  .flyer {
    position: absolute; left: 34px; top: 0;
    width: 928px; height: 1200px;
    background: var(--white); overflow: hidden;
  }
  .abs { position: absolute; }

  .kitchen-photo {
    position: absolute; left: 0; top: 0; width: 928px; height: 558px;
    clip-path: polygon(711px 0, 928px 0, 928px 558px, 709px 558px, 574px 277px);
    background:
      linear-gradient(180deg, rgba(255,255,255,0) 0%, rgba(255,255,255,0) 55%, rgba(120,128,134,.35) 56%, rgba(70,76,80,.6) 100%),
      linear-gradient(110deg, var(--steel-light) 0%, var(--steel-mid) 55%, var(--steel-dark) 100%);
  }
  .band-red {
    position: absolute; left: 0; top: 273px; width: 640px; height: 152px;
    background: var(--red);
    clip-path: polygon(0 0, 552px 0, 621px 152px, 0 152px);
  }
  .band-dark {
    position: absolute; left: 0; top: 425px; width: 700px; height: 133px;
    background: var(--ink);
    clip-path: polygon(0 0, 621px 0, 682px 133px, 0 133px);
  }

  .title-main {
    left: 66px; top: 54px;
    font-family: "Bebas Neue", sans-serif; color: var(--red);
    font-size: 128px; line-height: 1; letter-spacing: -1px;
  }
  .title-sub {
    left: 64px; top: 151px;
    font-weight: 700; color: var(--ink);
    font-size: 43px; line-height: 43px; letter-spacing: -0.8px; white-space: nowrap;
  }
  .band-heading {
    left: 64px; top: 285px;
    color: var(--white); font-weight: 700;
    font-size: 34.5px; line-height: 41px; white-space: nowrap;
  }
  .service-area {
    left: 64px; top: 374px;
    display: flex; align-items: center; gap: 10px;
    color: var(--ink); font-weight: 600; font-size: 25px; white-space: nowrap;
  }
  .front-to-back {
    left: 64px; top: 442px;
    font-family: "Bebas Neue", sans-serif; color: var(--white);
    font-size: 28px; white-space: nowrap;
    transform: scaleX(0.88); transform-origin: left center;
  }
  .quick-list { list-style: none; color: var(--white); font-weight: 700; font-size: 18px; }
  .quick-list li { position: absolute; white-space: nowrap; padding-left: 20px; }

  .tick { position: relative; }
  .tick::before {
    content: ""; position: absolute; left: 0; top: 50%;
    width: 13px; height: 13px; margin-top: -6.5px;
    border-radius: 50%; background: var(--red);
  }
  .tick::after {
    content: ""; position: absolute; left: 4px; top: 50%;
    width: 5px; height: 3px; margin-top: -3px;
    border-left: 2px solid var(--white); border-bottom: 2px solid var(--white);
    transform: rotate(-45deg);
  }
  .tick.dark::before { background: #111; }

  .section-title { font-weight: 700; font-size: 27px; line-height: 31px; color: var(--ink); }
  .section-title .accent { color: var(--red); }
  .hot-cold { left: 64px; top: 571px; }

  .equip-list { list-style: none; left: 71px; top: 636px; }
  .equip-list li {
    height: 35.2px; line-height: 24px; padding-left: 21px;
    font-size: 19px; color: var(--ink); white-space: nowrap;
  }
  .equip-list li::before, .equip-list li::after { top: 12px; }

  .why-box {
    left: 494px; top: 587px; width: 369px; height: 274px; background: var(--red);
  }
  .why-tab { left: 476px; top: 574px; width: 282px; height: 68px; }
  .why-title {
    left: 520px; top: 584px; color: var(--white); font-weight: 700; font-size: 22px;
  }
  .why-list { list-style: none; left: 519px; top: 641px; width: 340px; }
  .why-list li {
    position: absolute; left: 0; padding-left: 15px;
    color: var(--white); font-weight: 500; font-size: 14.4px; line-height: 17px; white-space: nowrap;
  }
  .why-list li::before, .why-list li::after { top: 9px; }

  .facility { left: 64px; top: 856px; }
  .facility-list { list-style: none; font-weight: 700; font-size: 15.3px; color: var(--ink); }
  .facility-list li { position: absolute; padding-left: 16px; line-height: 18px; white-space: nowrap; }
  .facility-list li::before, .facility-list li::after { top: 9px; }

  .cta-band {
    left: 0; top: 1050px; width: 470px; height: 68px; background: var(--red);
    clip-path: polygon(0 0, 412px 0, 469px 68px, 0 68px);
  }
  .cta-text {
    left: 64px; top: 1059px; color: var(--white); font-weight: 700;
    font-size: 25px; line-height: 25px; white-space: nowrap;
  }
  .fix-title { left: 489px; top: 1044px; color: var(--red); font-weight: 700; font-size: 28px; }
  .fix-sub { left: 489px; top: 1080px; color: var(--ink); font-weight: 700; font-size: 19px; white-space: nowrap; }

  .footer { left: 0; top: 1118px; width: 928px; height: 82px; background: var(--ink); }
  .phone {
    left: 64px; top: 1124px; display: flex; align-items: center; gap: 6px;
    color: var(--white); font-weight: 600; font-size: 33px;
  }
  .website {
    left: 398px; top: 1123px; display: flex; align-items: center; gap: 12px;
    color: var(--white); font-weight: 600; font-size: 25px; white-space: nowrap;
  }
  .website .name { color: var(--red); }
</style>
</head>
<body>
<main class="flyer">
  <div class="kitchen-photo" role="img" aria-label="Photo of a stainless steel commercial kitchen cooking line"></div>
  <div class="band-red"></div>
  <div class="band-dark"></div>

  <h1 class="abs title-main">RESTAURANT</h1>
  <p class="abs title-sub">FACILITYEQUIPMENT &amp;<br>STORE MAINTENANCE</p>

  <h2 class="abs band-heading">COMMERCIAL &amp; INDUSTRIAL<br>KITCHEN SERVICES</h2>
  <p class="abs service-area">
    <svg width="20" height="24" viewBox="0 0 20 24" aria-hidden="true">
      <path d="M10 1a7 7 0 0 1 7 7c0 5-7 11-7 11S3 13 3 8a7 7 0 0 1 7-7z" fill="#fff"/>
      <circle cx="10" cy="8" r="2.6" fill="#d11a2e"/>
      <ellipse cx="10" cy="21" rx="8" ry="2.2" fill="none" stroke="#fff" stroke-width="1.6"/>
    </svg>
    Denver Metro &amp; Surrounding Areas
  </p>

  <p class="abs front-to-back">WE HANDLE EVERYTHING FROM THE FRONT DOOR TO THE BACK DOOR</p>
  <ul class="quick-list">
    <li class="tick" style="left:66px;top:482px">OSHA Inspection</li>
    <li class="tick" style="left:417px;top:482px">Installation</li>
    <li class="tick" style="left:66px;top:517px">Preventive Maintenance</li>
    <li class="tick" style="left:417px;top:517px">Rebuilds</li>
  </ul>

  <h3 class="abs section-title hot-cold"><span class="accent">Hot &amp;&nbsp; Cold</span><br>Equipment Services</h3>
  <ul class="abs equip-list">
    <li class="tick">Installation, Repair &amp; Rebuilds</li>
    <li class="tick">Preventive Maintenance Programs</li>
    <li class="tick">Equipment Cleaning &amp; Refurbishing</li>
    <li class="tick">OEM Parts with 30-Day Warranty</li>
    <li class="tick">Used Equipment Sales &amp; Rentals</li>
    <li class="tick">CFESA-Certified Technicians</li>
  </ul>

  <div class="abs why-box"></div>
  <svg class="abs why-tab" viewBox="0 0 282 68" aria-hidden="true">
    <polygon points="0,0 262,0 281,53 18,53" fill="#000"/>
    <polygon points="0,53 18,53 18,68" fill="#000"/>
  </svg>
  <h3 class="abs why-title">Why Choose Us?</h3>
  <ul class="abs why-list">
    <li class="tick dark" style="top:2px">CFESA Certified Technicians</li>
    <li class="tick dark" style="top:35px">OEM Parts for Maximum Reliability</li>
    <li class="tick dark" style="top:67px">Preventive Maintenance Subscribers<br>Save on Labor Rates</li>
    <li class="tick dark" style="top:116px">Rapid Dispatch of Skilled Technicians</li>
    <li class="tick dark" style="top:148px">Local &amp; Trusted in the Denver Metro Area</li>
    <li class="tick dark" style="top:180px">Graffiti Removal Services Available</li>
  </ul>

  <h3 class="abs section-title facility"><span class="accent">Full Facility</span> Support</h3>
  <ul class="facility-list">
    <li class="tick" style="left:71px;top:896px">Emergency Repairs (24/7 Availability)</li>
    <li class="tick" style="left:71px;top:923px">OSHA Inspections</li>
    <li class="tick" style="left:71px;top:950px">Handyman Services</li>
    <li class="tick" style="left:71px;top:978px">Electrical Upgrades (Licensed Contractor)</li>
    <li class="tick" style="left:71px;top:1005px">Wall, Floor &amp; Ceiling Repairs</li>
    <li class="tick" style="left:497px;top:896px">Painting, Drywall, Door Closers</li>
    <li class="tick" style="left:497px;top:923px">Restaurant Furniture Repair/Replacement</li>
    <li class="tick" style="left:497px;top:950px">Décor, Signage, Parking Lot &amp; Dumpster<br>Area Repairs</li>
    <li class="tick" style="left:497px;top:996px">Food Service Truck Equipment Repairs</li>
  </ul>

  <div class="abs cta-band"></div>
  <p class="abs cta-text">CALL TODAY FOR FAST<br>PROFESSIONAL SERVICE</p>
  <p class="abs fix-title">WE FIX IT ALL</p>
  <p class="abs fix-sub">IF YOU HAVE IT, WE PROBABLY FIX IT.</p>

  <footer class="abs footer"></footer>
  <p class="abs phone">
    <svg width="22" height="22" viewBox="0 0 22 22" aria-hidden="true">
      <circle cx="11" cy="11" r="10" fill="#d11a2e"/>
      <path d="M7.5 5.5l2 2.3-1.2 1.5c.8 1.6 2 2.8 3.6 3.6l1.5-1.2 2.3 2-1.2 2c-4.3-.4-8.1-4.2-8.5-8.5z" fill="#fff"/>
    </svg>
    5550142198
  </p>
  <p class="abs website">
    <svg width="24" height="24" viewBox="0 0 24 24" aria-hidden="true">
      <circle cx="12" cy="12" r="11" fill="#d11a2e"/>
      <g fill="none" stroke="#232323" stroke-width="1.3">
        <circle cx="12" cy="12" r="6.5"/>
        <ellipse cx="12" cy="12" rx="3" ry="6.5"/>
        <line x1="5.5" y1="12" x2="18.5" y2="12"/>
      </g>
    </svg>
    <span>www.<span class="name">RapidKitchenCare</span>.com</span>
  </p>
</main>
</body>
</html>
```